Business Card Design Project

Mabel's Tonics is a natural skincare business and we need a business card designed. The company focuses on natural products and will be launching with body scrubs and bath fizzies and our mission statement is: To deliver high quality natural beauty products at a good value. It's two cards - one design - the only information changing would be name and email address

Target Market(s)

Females ages 20-50

Industry/Entity Type

Business

Requirements
Must have
• Mabel's Tonics

Corinne Halvorsen-Pitt
T: 800-417-9368
E: Corinne@MabelsTonics.example
W: www.MabelsTonics.example

Ulrich Benedetti
T: 800-417-9368
E: Ulrich@MabelsTonics.example
W: www.MabelsTonics.example
Nice to have
• I'd like to use the colors or text found at www.mabelstonics.example but I'm open to suggestions since design isn't set in stone yet. I would also like to have the words .....a little bit of magic somewhere under the company name in a different type of font. I would like a design that feels clean and maybe a retro feel to it - front and back would be nice but not mandatory

```html
<!DOCTYPE html>
<html lang="en">
<head>
<meta charset="utf-8">
<title>Mabel's Tonics — Business Card</title>
<link rel="stylesheet" href="https://fonts.googleapis.com/css2?family=Inter:wght@200;300;400&display=swap">
<style>
  :root {
    --paper: #ffffff;
    --ink: #000000;
    --muted: #6f6f6f;
    --linen: #c68aae;
    --rule: #111111;
  }
  html, body {
    margin: 0;
    padding: 0;
    width: 1200px;
    height: 900px;
    overflow: hidden;
    background: var(--paper);
  }
  .card {
    position: relative;
    width: 1200px;
    height: 900px;
    background: var(--paper);
    font-family: "Inter", "Helvetica Neue", Arial, sans-serif;
    color: var(--ink);
  }
  .side-band {
    position: absolute;
    top: 80px;
    height: 735px;
    width: 168px;
    background: var(--linen);
  }
  .side-band--left { left: 0; border-right: 4px solid var(--rule); }
  .side-band--right { right: 0; width: 172px; border-left: 4px solid var(--rule); }
  .brand {
    position: absolute;
    left: 172px;
    width: 852px;
    top: 118px;
    margin: 0;
    text-align: center;
    font-weight: 300;
    font-size: 168px;
    line-height: 160px;
    letter-spacing: 10px;
  }
  .brand span { display: block; }
  .tagline-rule {
    position: absolute;
    left: 513px;
    width: 173px;
    height: 0;
    border-top: 1.5px solid var(--ink);
  }
  .tagline-rule--top { top: 506px; }
  .tagline-rule--bottom { top: 592px; }
  .tagline {
    position: absolute;
    left: 172px;
    width: 852px;
    top: 522px;
    margin: 0;
    text-align: center;
    font-weight: 400;
    font-size: 43px;
    line-height: 52px;
  }
  .contact {
    position: absolute;
    left: 172px;
    width: 852px;
    top: 622px;
    margin: 0;
    text-align: center;
    font-weight: 300;
    font-size: 33px;
    line-height: 42px;
    letter-spacing: 2px;
    color: var(--muted);
    font-style: normal;
  }
  .contact p { margin: 0; }
</style>
</head>
<body>
  <main class="card">
    <div class="side-band side-band--left" role="img" aria-label="Mauve linen texture band"></div>
    <div class="side-band side-band--right" role="img" aria-label="Mauve linen texture band"></div>

    <h1 class="brand"><span>Mabel’s</span><span>Tonics</span></h1>

    <div class="tagline-rule tagline-rule--top"></div>
    <p class="tagline">a little big of magic</p>
    <div class="tagline-rule tagline-rule--bottom"></div>

    <address class="contact">
      <p class="contact__name">Corinne Halvorsen-Pitt</p>
      <p class="contact__phone">T: 800-417-9368</p>
      <p class="contact__email">E: Corinne@MabelsTonics.example</p>
      <p class="contact__web">W: www.MabelsTonics.example</p>
    </address>
  </main>
</body>
</html>
```